Business Card Design for Consulting Company

I require a Business Card design for my Consulting company. <br/><br/>My company name is: Marek Olvani Consulting Inc.<br/>My website is: www.marekolvaniconsulting.example<br/><br/>My company focuses on management and software development for the Tallobrix CRM platform (www.tallobrix.example)<br/><br/>I have a logo already designed...see attached.
Updates

Also Include my Name and Title: Marek T.L. Olvani President

Target Market(s)

Tallobrix Customers

Contact Information for Business Card

Only include my LOGO (provided)
My Name: Marek TL Olvani
My Title: President
My Company Name: Marek Olvani Consulting Inc.
My Website: www.marekolvaniconsulting.example
My Email: marek.olvani.consulting@mailbox.example

NO PHONE NUMBER
NO ADDRESS

Font styles to use
Serif
Sans Serif
Other font styles liked:
• see my website: www.marekolvaniconsulting.example

Colors

Designer to choose colors to be used in the design.

Requirements
Must have
• Must include my Orange
• Include my name (Marek T.L. Olvani), title (President) company name, website and email
• It should also have a tag line like: Tallobrix Consulting
• I'm flexible with the tag line
Should not have
• Don't include my phone number or address

```html
<!DOCTYPE html>
<html lang="en">
<head>
<meta charset="utf-8">
<title>Marek Olvani Consulting Inc. – Business Card</title>
<link rel="stylesheet" href="https://fonts.googleapis.com/css2?family=Source+Sans+3:wght@400;600;700&display=swap">
<style>
  :root {
    --brand-orange: #fa8404;
    --card-edge: #fcd9b0;
    --ink: #000000;
    --ink-soft: #333333;
    --paper: #ffffff;
    --globe-blue: #1a7cc4;
  }
  html, body {
    margin: 0;
    padding: 0;
    width: 1200px;
    height: 1200px;
    overflow: hidden;
    background: var(--paper);
  }
  .canvas {
    position: relative;
    width: 1200px;
    height: 1200px;
    font-family: "Source Sans 3", sans-serif;
  }
  .card-shapes {
    position: absolute;
    inset: 0;
    width: 1200px;
    height: 1200px;
  }
  .brand-mark {
    position: absolute;
    left: 174px;
    top: 318px;
    width: 323px;
    height: 165px;
    display: flex;
    align-items: center;
    justify-content: center;
    font-weight: 700;
    font-size: 150px;
    line-height: 1;
    color: var(--brand-orange);
    letter-spacing: -2px;
  }
  .company-name {
    position: absolute;
    left: 63px;
    top: 488px;
    margin: 0;
    font-weight: 700;
    font-size: 46px;
    line-height: 1;
    color: var(--ink);
    white-space: nowrap;
    letter-spacing: -0.3px;
  }
  .person {
    position: absolute;
    left: 66px;
    top: 580px;
    margin: 0;
    line-height: 1;
    white-space: nowrap;
  }
  .person-name {
    display: block;
    font-weight: 700;
    font-size: 30px;
    color: var(--ink);
  }
  .person-title {
    display: block;
    margin-top: 8px;
    font-weight: 400;
    font-size: 24px;
    color: var(--ink-soft);
  }
  .tagline {
    position: absolute;
    left: 66px;
    top: 680px;
    margin: 0;
    font-weight: 600;
    font-size: 24px;
    line-height: 1;
    color: var(--brand-orange);
    white-space: nowrap;
  }
  .contact-line {
    position: absolute;
    left: 492px;
    width: 600px;
    margin: 0;
    text-align: center;
    color: var(--paper);
    font-weight: 400;
    line-height: 1;
    white-space: nowrap;
  }
  .contact-web { top: 706px; font-size: 32px; }
  .contact-email { top: 839px; font-size: 31px; }
</style>
</head>
<body>
<main class="canvas">
  <svg class="card-shapes" viewBox="0 0 1920 1920" aria-hidden="true">
    <rect class="card-outline" x="43.5" y="462.5" width="1843" height="1005" fill="none" stroke="var(--card-edge)" stroke-width="1.5"/>
    <path class="orange-sweep" fill="var(--brand-orange)"
      d="M627 1469 C575 1415 537 1355 537 1290 C537 1050 960 876 1420 876 C1610 876 1760 898 1888 934 L1888 1463 Z"/>
    <g class="icon-web">
      <circle cx="1267" cy="1049" r="68" fill="var(--globe-blue)"/>
      <circle cx="1267" cy="1049" r="56" fill="none" stroke="var(--paper)" stroke-width="5"/>
      <line x1="1267" y1="993" x2="1267" y2="1105" stroke="var(--paper)" stroke-width="5"/>
      <ellipse cx="1267" cy="1049" rx="26" ry="56" fill="none" stroke="var(--paper)" stroke-width="4"/>
      <rect x="1223" y="1033" width="88" height="32" rx="14" fill="var(--globe-blue)" stroke="var(--paper)" stroke-width="3"/>
      <text x="1267" y="1057" text-anchor="middle" font-family="Source Sans 3, sans-serif" font-size="24" font-weight="700" fill="var(--paper)">www</text>
    </g>
    <g class="icon-mail">
      <rect x="1207" y="1233" width="130" height="94" rx="5" fill="none" stroke="var(--paper)" stroke-width="7"/>
      <polyline points="1210,1238 1272,1286 1334,1238" fill="none" stroke="var(--paper)" stroke-width="7" stroke-linejoin="round"/>
    </g>
  </svg>

  <div class="brand-mark">MO</div>
  <h1 class="company-name">Marek Olvani Consulting Inc.</h1>
  <p class="person">
    <span class="person-name">Marek T.L. Olvani</span>
    <span class="person-title">President</span>
  </p>
  <p class="tagline">Tallobrix Consulting</p>
  <p class="contact-line contact-web">www.marekolvaniconsulting.example</p>
  <p class="contact-line contact-email">marek.olvani.consulting@mailbox.example</p>
</main>
</body>
</html>
```